brand new Logo and business card

Need a brand new simple logo and business card for my finance business, under business name Kestrel Lending Partners. xxxxxxxxxxxxxxxxxxxxxxxxxxxxxxxxxxxxxxxxxxxxxxxxxxxxxxxxxxxxxxxxxxxxxxxxxxxxxxxxxxxxxxxxxxxxxxxxxxxxxxxxxxxxxxxxxxxxxxxxxxxxxxxxxxxxxxxxxxxxxxxxxxxxxxxxxxxxxxxxxxxxxxxx

Target Market(s)

all

Industry/Entity Type

Finance

Contact Information for Business Card

Need a brand new simple logo and business card for my finance business, under business name Kestrel Lending Partners. xxxxxxxxxxxxxxxxxxxxxxxxxxxxxxxxxxxxxxxxxxxxxxxxxxxxxxxxxxxxxxxxxxxxxxxxxxxxxxxxxxxxxxxxxxxxxxxxxxxxxxxxxxxxxxxxxxxxxxxxxxxxxxxx

Logo Text

Kestrel Lending Partners Home Loans | Plant & Equipment | Automotive | Business & Commercial | Personal

Logo styles of interest
Wordmark Logo
Lettermark Logo
Font styles to use
Serif
Sans Serif

Requirements
Must have
• Tobias Crane Managing Director
• kestrellendingpartners.example.com.au
• tobias@kestrellendingpartners.example.com.au
• 0455 921 037 8am-9pm 7 Days
Nice to have
• nothing here to add
Should not have
• physical address

```html
<!DOCTYPE html>
<html lang="en">
<head>
<meta charset="utf-8">
<title>Kestrel Lending Partners — Business Card</title>
<link rel="stylesheet" href="https://fonts.googleapis.com/css2?family=Michroma&display=swap">
<style>
  :root {
    --backdrop: #d9dadc;
    --card: #ffffff;
    --brand-blue: #1f4f95;
    --text-grey: #6d6f73;
    --band-grey: #ededee;
    --rule-grey: #9a9ca0;
  }
  * { box-sizing: border-box; margin: 0; padding: 0; }
  html, body {
    width: 1200px;
    height: 848px;
    overflow: hidden;
    background: var(--backdrop);
    font-family: "Michroma", sans-serif;
  }
  .stage {
    width: 1200px;
    height: 848px;
    display: flex;
    align-items: center;
    justify-content: center;
  }
  .business-card {
    position: relative;
    width: 900px;
    height: 514px;
    background: var(--card);
    box-shadow: 0 10px 30px rgba(0,0,0,0.18);
    overflow: hidden;
  }
  .brand {
    position: absolute;
    left: 56px;
    top: 42px;
    display: flex;
    align-items: flex-start;
    gap: 14px;
  }
  .brand-square {
    width: 34px;
    height: 34px;
    background: var(--brand-blue);
    margin-top: 4px;
  }
  .brand-name {
    color: var(--brand-blue);
    font-size: 13px;
    line-height: 1.45;
    letter-spacing: 0.08em;
    text-transform: uppercase;
  }
  .services {
    position: absolute;
    right: 50px;
    top: 54px;
    text-align: right;
    color: var(--text-grey);
    font-size: 11px;
    line-height: 2;
    letter-spacing: 0.06em;
    text-transform: uppercase;
  }
  .services .bar { color: var(--rule-grey); padding: 0 6px; }
  .person {
    position: absolute;
    left: 230px;
    top: 212px;
  }
  .person-name {
    color: var(--brand-blue);
    font-size: 34px;
    letter-spacing: 0.06em;
    text-transform: uppercase;
  }
  .person-title {
    margin-top: 8px;
    margin-left: 4px;
    color: var(--text-grey);
    font-size: 13px;
    letter-spacing: 0.08em;
    text-transform: uppercase;
  }
  .contact-band {
    position: absolute;
    left: 0;
    right: 0;
    top: 330px;
    height: 92px;
    background: var(--band-grey);
    padding: 20px 0 0 56px;
    color: var(--brand-blue);
    font-size: 13px;
    line-height: 2.1;
    letter-spacing: 0.05em;
    text-transform: uppercase;
  }
  .contact-band .hours { margin-left: 34px; }
  .web-band {
    position: absolute;
    left: 0;
    right: 0;
    top: 422px;
    height: 46px;
    background: var(--brand-blue);
    color: #ffffff;
    padding-left: 56px;
    font-size: 15px;
    line-height: 46px;
    letter-spacing: 0.07em;
    text-transform: uppercase;
  }
</style>
</head>
<body>
<main class="stage">
  <article class="business-card">
    <header class="brand">
      <span class="brand-square"></span>
      <span class="brand-name">Kestrel<br>Lending<br>Partners</span>
    </header>

    <p class="services">
      <span class="bar">|</span>Home Loans<span class="bar">|</span>Plant &amp; Equipment<span class="bar">|</span><br>
      <span class="bar">|</span>Automotive<span class="bar">|</span>Business &amp; Commercial<span class="bar">|</span><br>
      Personal<span class="bar">|</span>
    </p>

    <section class="person">
      <h1 class="person-name">Tobias Crane</h1>
      <p class="person-title">Managing Director</p>
    </section>

    <section class="contact-band">
      <p class="email">tobias@kestrellendingpartners.example.com.au</p>
      <p class="phone">0455 921 037<span class="hours">8am - 9pm / 7 Days</span></p>
    </section>

    <footer class="web-band">kestrellendingpartners.example.com.au</footer>
  </article>
</main>
</body>
</html>
```